A property investment company, looking to provide lovely sustainable homes for familys and individua

For a small investment business i am starting which will buy and refurbish unloved houses and apartments to rent out or resell. the company name is my family surname (HARGREAVE). <br/>i would like the design to be simple with maybe some emphasis on an ethical and sustainable/environmentally friendly approach with a branding of maybe trees blended with some houses and or apartments.<br/>The colours i like for this design would be mainly green on either a white or black background.
Target Market(s)
This business card is to be used for professional people such as estate agents
mortgage brokers, solicitors and trades people.
Industry/Entity Type
Real Estate
Contact Information for Business Card
owner/director-Martin hargreave
e-mail-martin@hvholdings.co.uk
website-hargreavehomeholdings.co.uk
mobile-07700945318
landline-02079460581
Look and feel

```html
<!DOCTYPE html>
<html lang="en">
<head>
<meta charset="utf-8">
<title>Hargreave – Business Card</title>
<link href="https://fonts.googleapis.com/css2?family=Montserrat:wght@400;500;700;800&display=swap" rel="stylesheet">
<style>
  :root {
    --backdrop: #2e2a29;
    --card-white: #ffffff;
    --card-grey: #5f6569;
    --ink: #1f1f1f;
    --green: #8dc63f;
    --teal: #2bb5a0;
    --rule: #e2e2e2;
  }
  * { margin: 0; padding: 0; box-sizing: border-box; }
  html, body {
    width: 1200px; height: 912px; overflow: hidden;
    background: var(--backdrop);
    font-family: "Montserrat", sans-serif;
  }
  .canvas { position: relative; width: 1200px; height: 912px; }
  .card {
    position: absolute; width: 620px; height: 370px;
    box-shadow: 0 10px 30px rgba(0,0,0,.35);
  }
  .card--front { left: 110px; top: 60px; background: var(--card-white); }
  .card--back { left: 470px; top: 482px; background: var(--card-grey); }

  .front-brand {
    position: absolute; top: 30px; right: 34px;
    display: flex; align-items: center; gap: 8px;
    font-weight: 800; font-size: 16px; letter-spacing: .06em; color: var(--green);
  }
  .brand-square { width: 14px; height: 14px; background: var(--teal); }

  .holder { position: absolute; left: 40px; top: 222px; }
  .holder__name { font-weight: 700; font-size: 21px; color: var(--ink); }
  .holder__role { font-weight: 500; font-size: 13px; color: var(--green); margin-top: 3px; }

  .divider {
    position: absolute; left: 40px; right: 34px; top: 280px;
    height: 1px; background: var(--rule);
  }

  .contact { position: absolute; font-size: 13px; color: var(--ink); }
  .contact li { list-style: none; display: flex; align-items: center; gap: 9px; height: 24px; }
  .contact svg { width: 14px; height: 14px; flex: none; }
  .contact--phones { left: 40px; top: 294px; }
  .contact--web { right: 34px; top: 294px; }
  .contact--web li { justify-content: flex-end; }

  .back-brand {
    position: absolute; inset: 0;
    display: flex; align-items: center; justify-content: center; gap: 18px;
    font-weight: 800; font-size: 52px; letter-spacing: .04em; color: #ffffff;
  }
  .back-brand .brand-square { width: 40px; height: 40px; background: var(--green); }
</style>
</head>
<body>
<main class="canvas">
  <section class="card card--front" aria-label="Business card, contact side">
    <div class="front-brand"><span class="brand-square"></span>HARGREAVE</div>

    <div class="holder">
      <p class="holder__name">Martin Hargreave</p>
      <p class="holder__role">Owner/Director</p>
    </div>

    <div class="divider"></div>

    <ul class="contact contact--phones">
      <li>
        <svg viewBox="0 0 14 14" aria-hidden="true"><rect x="3.5" y="1" width="7" height="12" rx="1.5" fill="none" stroke="#2bb5a0" stroke-width="1.4"/><circle cx="7" cy="11" r=".8" fill="#2bb5a0"/></svg>
        07700945318
      </li>
      <li>
        <svg viewBox="0 0 14 14" aria-hidden="true"><path d="M3 1.5l2.2 2.6-1.2 1.6c.9 1.9 2.3 3.3 4.2 4.2l1.6-1.2 2.6 2.2-1.4 1.8C6 12.3 1.7 8 1.2 3z" fill="#2bb5a0"/></svg>
        02079460581
      </li>
    </ul>

    <ul class="contact contact--web">
      <li>
        martin@hvholdings.co.uk
        <svg viewBox="0 0 14 14" aria-hidden="true"><rect x="1" y="3" width="12" height="8.5" rx="1" fill="#2bb5a0"/><path d="M1.5 3.6L7 8l5.5-4.4" fill="none" stroke="#fff" stroke-width="1.1"/></svg>
      </li>
      <li>
        hargreavehomeholdings.co.uk
        <svg viewBox="0 0 14 14" aria-hidden="true"><circle cx="7" cy="7" r="5.8" fill="none" stroke="#2bb5a0" stroke-width="1.3"/><ellipse cx="7" cy="7" rx="2.5" ry="5.8" fill="none" stroke="#2bb5a0" stroke-width="1"/><path d="M1.2 7h11.6" stroke="#2bb5a0" stroke-width="1"/></svg>
      </li>
    </ul>
  </section>

  <section class="card card--back" aria-label="Business card, brand side">
    <div class="back-brand"><span class="brand-square"></span>HARGREAVE</div>
  </section>
</main>
</body>
</html>
```